New, modern business card for growing audiology practice

We need a new business card for our audiology practice. Our logo and website have recently changed (more modern) and we want our business cards to reflect this change.
We conduct hearing tests, perform earwax removals, and fit & dispense hearing aids to our patients. We are a family owned practice in which the owner is the one who works directly with the patient. I have attached logos in various formats to use, as well as two ideas I found on this website; as well as a scanned copy of our current logo. Good luck!

Industry/Entity Type

Business

Contact Information for Business Card

Company name: Maplow Hearing Center
Provider name: Peter Mulvoy, Au.D. F/ISN
Phone number: (555) 318-6042
Address: 87 W. Linden Ave. Alderbrook, OH 44190
email: maplowhearing@postvale.net
website: maplowhearing.com

Colors
000000
aaaaaa
dbdbdb
cacaca
9bcb3c
afd23c
cadf82
b1b1b1

Requirements
Must have
• My card must include information in the "details" section. In the attached images, I found a few that I liked and I would like to model after - "brisk tumblin'" and "Sound Wellness Center".
• Must be horizontal.
• Must include logos provided. I uploaded them in various file formats and various ways.
• Must match logo font, if possible, if not, please get as close as you can.
Nice to have
• I really like the idea of having a color on one side with just the logo and company name and the contact information and provider name on the other side. I also really like the idea of having the main color dominating on the logo/company side with accent of that same color on the contact side of the card.
Should not have
• Must not be vertical.

```html
<!DOCTYPE html>
<html lang="en">
<head>
<meta charset="utf-8">
<title>Maplow Hearing Center – Business Card</title>
<link rel="stylesheet" href="https://fonts.googleapis.com/css2?family=Lato:wght@400&family=Montserrat:wght@400;700&display=swap">
<style>
  :root {
    --brand-green: #7ca443;
    --ink: #111111;
    --paper: #ffffff;
    --edge: #d6d6d6;
  }
  * { margin: 0; padding: 0; box-sizing: border-box; }
  html, body { width: 1200px; height: 1000px; overflow: hidden; background: var(--paper); }
  .canvas { position: relative; width: 1200px; height: 1000px; }

  .card { position: absolute; width: 510px; height: 306px; overflow: hidden; }

  .card--front { left: 344px; top: 188px; background: var(--brand-green); }
  .card--back { left: 346px; top: 506px; background: var(--paper); border: 1px solid var(--edge); }

  .wordmark {
    position: absolute;
    display: flex; align-items: center; gap: 10px;
    font-family: "Lato", "Gill Sans", sans-serif;
    font-weight: 400; letter-spacing: -0.3px;
    white-space: nowrap;
  }
  .wordmark__dot { width: 22px; height: 22px; border-radius: 50%; flex: none; }
  .card--front .wordmark { left: 56px; top: 140px; font-size: 28px; color: var(--paper); }
  .card--front .wordmark__dot { background: var(--paper); }
  .card--back .wordmark { left: 47px; top: 52px; font-size: 29px; color: var(--ink); }
  .card--back .wordmark__dot { background: var(--brand-green); }

  .card__bands { position: absolute; inset: 0; }

  .contact {
    position: absolute; left: 44px; top: 145px;
    font-family: "Montserrat", sans-serif; font-size: 15px; color: var(--ink);
    list-style: none; line-height: 19.5px;
  }
  .contact li { display: flex; align-items: center; gap: 6px; }
  .contact__icon { width: 14px; height: 14px; flex: none; }
  .contact__indent { padding-left: 20px; }
  .contact__name { font-weight: 700; font-size: 15.5px; }
  .contact__cred { font-weight: 700; font-size: 12.5px; }
</style>
</head>
<body>
<main class="canvas">

  <section class="card card--front" aria-label="Card front">
    <div class="wordmark"><span class="wordmark__dot"></span>MAPLOW HEARING CENTER</div>
  </section>

  <section class="card card--back" aria-label="Card back">
    <svg class="card__bands" viewBox="0 0 510 306" width="510" height="306" aria-hidden="true">
      <path d="M0 0 H510 V42 Q255 2 0 42 Z" fill="var(--brand-green)"/>
      <path d="M0 264 Q255 308 510 264 V306 H0 Z" fill="var(--brand-green)"/>
    </svg>

    <div class="wordmark"><span class="wordmark__dot"></span>MAPLOW HEARING CENTER</div>

    <ul class="contact">
      <li>
        <svg class="contact__icon" viewBox="0 0 14 14" aria-hidden="true"><rect x="3.5" y="1" width="7" height="12" rx="1.5" fill="var(--brand-green)"/><rect x="5" y="3" width="4" height="4" fill="#fff"/></svg>
        <span><span class="contact__name">Peter Mulvoy,</span> <span class="contact__cred">Au.D. F/ISN</span></span>
      </li>
      <li class="contact__indent">(555) 318-6042</li>
      <li>
        <svg class="contact__icon" viewBox="0 0 14 14" aria-hidden="true"><path d="M7 1.5 L13 7 H11 V12.5 H8.5 V9 H5.5 V12.5 H3 V7 H1 Z" fill="var(--brand-green)"/></svg>
        <span>87 W. Linden Ave. Alderbrook, OH 44190</span>
      </li>
      <li>
        <svg class="contact__icon" viewBox="0 0 14 14" aria-hidden="true"><rect x="1" y="3" width="12" height="8.5" rx="1" fill="var(--brand-green)"/><path d="M1.5 3.5 L7 7.8 L12.5 3.5" stroke="#fff" stroke-width="1" fill="none"/></svg>
        <span>maplowhearing@postvale.net</span>
      </li>
      <li>
        <svg class="contact__icon" viewBox="0 0 14 14" aria-hidden="true"><circle cx="7" cy="7" r="6" fill="var(--brand-green)"/><g stroke="#fff" stroke-width="0.8" fill="none"><ellipse cx="7" cy="7" rx="2.5" ry="6"/><path d="M1 7 H13 M2 4 H12 M2 10 H12"/></g></svg>
        <span>www.maplowhearing.com</span>
      </li>
    </ul>
  </section>

</main>
</body>
</html>
```